Dr. Marisa Tellen Medical/Chiropractic Business Card

Dr. Tellen is a chiropractor and will require a business card that she uses every single day to book appointments on the back side of the card. Currently the office name goes by Dr. Marisa Tellen. The chiropractic profession is based on the diagnosis and manipulative treatment of misalignments of the joints, especially those of the spinal column, which are held to cause other disorders by affecting the nerves, muscles, and organs. Dr. Marisa Tellen is looking for a contemporary and minimalistic design.

Industry/Entity Type

Medical

Contact Information for Business Card

Name: Dr. Marisa Tellen; Address: 748 Ashcombe Rd North, London, ON N5R 2K9; Phone Number: 519.672.4193; Fax: 519.681.2054; email: marisa.tellen@brevanmail.com

Requirements
Must have
• ability to write multiple appointments date/time on the back of card

```html
<!DOCTYPE html>
<html lang="en">
<head>
<meta charset="utf-8">
<title>Dr. Marisa Tellen – Business Card</title>
<link rel="stylesheet" href="https://fonts.googleapis.com/css2?family=Fira+Sans:wght@400;500;600&family=Arimo:wght@400&display=swap">
<style>
  :root {
    --page-bg: #6b7789;
    --card-white: #ffffff;
    --card-grey: #dcdee2;
    --rule-line: rgba(170, 178, 190, 0.28);
    --brand-blue: #1276c0;
    --brand-blue-light: #5d9fd6;
    --brand-navy: #262f8f;
    --text-grey: #4a4d52;
  }
  * { margin: 0; padding: 0; box-sizing: border-box; }
  html, body {
    width: 1200px; height: 1200px; overflow: hidden;
    background: var(--page-bg);
  }
  .sheet {
    width: 1200px; height: 1200px;
    display: flex; flex-direction: column;
    align-items: center; justify-content: center; gap: 44px;
  }
  .card {
    position: relative;
    width: 900px; height: 514px;
    background:
      repeating-linear-gradient(to bottom, transparent 0 23px, var(--rule-line) 23px 24px),
      linear-gradient(100deg, var(--card-white) 35%, var(--card-grey) 85%);
    box-shadow: 0 10px 28px rgba(20, 28, 40, 0.35);
    overflow: hidden;
  }
  .card svg { position: absolute; inset: 0; width: 100%; height: 100%; }
  .band { fill: var(--brand-blue); }
  .band-rule { stroke: var(--brand-navy); stroke-width: 7; }
  .band-name {
    font-family: "Fira Sans", sans-serif; font-weight: 500;
    font-size: 64px; fill: var(--brand-blue-light);
  }
  .contact {
    font-family: "Arimo", sans-serif; font-size: 25px; fill: var(--text-grey);
  }
  .icon-ring { fill: none; stroke: var(--brand-blue); stroke-width: 2.4; }
  .icon-mark { fill: var(--brand-blue); }
  .icon-line { fill: none; stroke: var(--brand-blue); stroke-width: 2; }
  .name-rule { stroke: var(--brand-blue); stroke-width: 1.6; }
  .card-name {
    font-family: "Fira Sans", sans-serif; font-weight: 600;
    font-size: 70px; fill: var(--brand-blue);
  }
  .card-name-reflection { opacity: 0.1; }
  .appointments-title {
    font-family: "Fira Sans", sans-serif; font-weight: 500;
    font-size: 30px; letter-spacing: 1px; fill: var(--brand-blue);
  }
  .slot-label {
    font-family: "Fira Sans", sans-serif; font-size: 21px; fill: var(--brand-blue);
  }
  .slot-line {
    stroke: var(--brand-blue); stroke-width: 1.8; stroke-dasharray: 1.6 4;
    stroke-linecap: round;
  }
</style>
</head>
<body>
<main class="sheet">

  <section class="card card-front" aria-label="Business card front">
    <svg viewBox="0 0 900 514">
      <polygon class="band" points="606,0 900,0 900,514 786,514"/>
      <line class="band-rule" x1="588" y1="0" x2="768" y2="514"/>
      <text class="band-name" transform="translate(866,494) rotate(-90)">Dr. Marisa Tellen</text>

      <g class="contact-row">
        <circle class="icon-ring" cx="58" cy="212" r="11"/>
        <path class="icon-mark" d="M51 214 q7 -9 14 0 l-2 3 h-10 z"/>
        <text class="contact" x="80" y="221">519.672.4193</text>
      </g>
      <g class="contact-row">
        <circle class="icon-ring" cx="58" cy="254" r="11"/>
        <rect class="icon-line" x="52" y="250" width="12" height="8"/>
        <rect class="icon-line" x="54.5" y="246" width="7" height="4"/>
        <text class="contact" x="80" y="263">519.681.2054</text>
      </g>
      <g class="contact-row">
        <circle class="icon-ring" cx="58" cy="312" r="11"/>
        <rect class="icon-line" x="51" y="307" width="14" height="10"/>
        <path class="icon-line" d="M51 307 l7 6 l7 -6"/>
        <text class="contact" x="80" y="321">marisa.tellen@brevanmail.com</text>
      </g>
      <g class="contact-row">
        <circle class="icon-ring" cx="58" cy="372" r="11"/>
        <path class="icon-mark" d="M58 380 l-5 -8 a5.5 5.5 0 1 1 10 0 z"/>
        <circle cx="58" cy="369" r="2" fill="#fff"/>
        <text class="contact" x="80" y="381">748 Ashcombe Rd North, London, ON N5R 2K9</text>
      </g>

      <line class="name-rule" x1="40" y1="404" x2="650" y2="404"/>
      <text class="card-name" x="40" y="476">Dr. Marisa Tellen</text>
      <text class="card-name card-name-reflection" transform="translate(0,960) scale(1,-1)" x="40" y="476" aria-hidden="true">Dr. Marisa Tellen</text>
    </svg>
  </section>

  <section class="card card-back" aria-label="Business card back, appointment slots">
    <svg viewBox="0 0 900 514">
      <polygon class="band" points="590,0 900,0 900,514 770,514"/>
      <line class="band-rule" x1="572" y1="0" x2="752" y2="514"/>
      <text class="band-name" transform="translate(836,22) rotate(90)">Dr. Marisa Tellen</text>

      <text class="appointments-title" x="44" y="74">APPOINTMENTS</text>

      <g class="slot">
        <text class="slot-label" x="60" y="150">Date</text>
        <line class="slot-line" x1="112" y1="146" x2="300" y2="146"/>
        <text class="slot-label" x="318" y="150">Time</text>
        <line class="slot-line" x1="372" y1="146" x2="560" y2="146"/>
      </g>
      <g class="slot">
        <text class="slot-label" x="60" y="218">Date</text>
        <line class="slot-line" x1="112" y1="214" x2="300" y2="214"/>
        <text class="slot-label" x="318" y="218">Time</text>
        <line class="slot-line" x1="372" y1="214" x2="560" y2="214"/>
      </g>
      <g class="slot">
        <text class="slot-label" x="60" y="286">Date</text>
        <line class="slot-line" x1="112" y1="282" x2="300" y2="282"/>
        <text class="slot-label" x="318" y="286">Time</text>
        <line class="slot-line" x1="372" y1="282" x2="580" y2="282"/>
      </g>
      <g class="slot">
        <text class="slot-label" x="60" y="354">Date</text>
        <line class="slot-line" x1="112" y1="350" x2="300" y2="350"/>
        <text class="slot-label" x="318" y="354">Time</text>
        <line class="slot-line" x1="372" y1="350" x2="600" y2="350"/>
      </g>
      <g class="slot">
        <text class="slot-label" x="60" y="422">Date</text>
        <line class="slot-line" x1="112" y1="418" x2="300" y2="418"/>
        <text class="slot-label" x="318" y="422">Time</text>
        <line class="slot-line" x1="372" y1="418" x2="620" y2="418"/>
      </g>
    </svg>
  </section>

</main>
</body>
</html>
```